Bref créative
RKT Stationery
B-Cards
I need double sided standard sized Business Card [3.5" x 2"]
Arial, Arial Black, Comic Sans MS, Courier New, Impact, Trebuchet MS and Verdana
Professional
Dorian Vasko
Operations Manager
P.O. BOX 817
Glenn Dale, MD 20769
dorian@rktbuilders.example
www.rktbuilders.example
Doesn't have to include all the information.
Atleast Company name, Logo, persons name and title.
Office number, cell, fax, and e-mail
Could have a calendar of the year, maybe QR codes for website, cell or e-mails of contact.
Anything else that could maybe go on the back of the card. I just don't want it to be blank.
vector logo file

```html
<!DOCTYPE html>
<html lang="en">
<head>
<meta charset="UTF-8">
<title>RKT Construction Business Cards</title>
<link rel="stylesheet" href="https://fonts.googleapis.com/css2?family=Montserrat:wght@400;600;700&display=swap">
<style>
  :root {
    --backdrop: #e4e4e2;
    --card: #ffffff;
    --card-shade: #f1f1ef;
    --red: #9b1424;
    --red-deep: #7c0d1a;
    --green: #3f7d1c;
    --ink: #3a3a3a;
    --soft-ink: #6b6b6b;
    --on-red: #ffffff;
  }
  * { margin: 0; padding: 0; box-sizing: border-box; }
  html, body {
    width: 1200px;
    height: 864px;
    overflow: hidden;
    background: var(--backdrop);
    font-family: "Montserrat", "Trebuchet MS", sans-serif;
  }
  .sheet { position: relative; width: 1200px; height: 864px; }
  .card {
    position: absolute;
    width: 525px;
    height: 300px;
    border-radius: 16px;
    background: linear-gradient(135deg, var(--card) 0%, var(--card) 60%, var(--card-shade) 100%);
    box-shadow: 0 10px 28px rgba(0,0,0,0.22);
    overflow: hidden;
  }
  .card--front { left: 50px; top: 150px; }
  .card--back { left: 625px; top: 414px; }

  /* front */
  .front-brand {
    position: absolute;
    left: 0; right: 0; top: 110px;
    display: flex;
    justify-content: center;
    align-items: center;
    gap: 10px;
  }
  .brand-mark { width: 20px; height: 20px; background: var(--red); }
  .brand-name {
    font-weight: 700;
    font-size: 26px;
    color: var(--red);
    letter-spacing: 1px;
  }
  .front-web {
    position: absolute;
    left: 0; right: 0; top: 168px;
    text-align: center;
    font-size: 13px;
    letter-spacing: 3px;
    color: var(--soft-ink);
  }

  /* back */
  .back-art { position: absolute; inset: 0; width: 525px; height: 300px; }
  .back-brand {
    position: absolute;
    left: 30px; top: 112px;
    display: flex;
    align-items: center;
    gap: 8px;
  }
  .back-brand .brand-mark { width: 14px; height: 14px; }
  .back-brand .brand-name { font-size: 16px; }
  .person { position: absolute; left: 30px; top: 150px; }
  .person-name {
    font-weight: 600;
    font-size: 16px;
    letter-spacing: 1.2px;
    color: var(--red);
  }
  .person-title {
    margin-top: 4px;
    font-size: 9px;
    letter-spacing: 1.8px;
    text-transform: uppercase;
    color: var(--soft-ink);
  }
  .contact {
    position: absolute;
    right: 22px; top: 30px;
    width: 140px;
    list-style: none;
    color: var(--on-red);
    font-size: 9px;
    line-height: 15px;
    text-align: right;
  }
  .contact li { display: flex; justify-content: flex-end; align-items: center; gap: 6px; white-space: nowrap; }
  .contact-dot { width: 4px; height: 4px; border-radius: 50%; background: var(--on-red); flex: none; }
</style>
</head>
<body>
<main class="sheet">
  <section class="card card--front" aria-label="Card front">
    <div class="front-brand">
      <span class="brand-mark"></span>
      <span class="brand-name">RKT Construction</span>
    </div>
    <p class="front-web">www.rktbuilders.example</p>
  </section>

  <section class="card card--back" aria-label="Card back">
    <svg class="back-art" viewBox="0 0 525 300" aria-hidden="true">
      <path d="M360 0 C330 160 230 250 0 268 L0 300 L525 300 L525 0 Z" fill="var(--red)"/>
      <path d="M372 0 C342 165 240 258 0 276 L0 300 L525 300 L525 0 Z" fill="var(--red-deep)" opacity="0.25"/>
      <path d="M340 0 C310 150 215 238 0 254" fill="none" stroke="var(--green)" stroke-width="7"/>
    </svg>
    <div class="back-brand">
      <span class="brand-mark"></span>
      <span class="brand-name">RKT Construction</span>
    </div>
    <div class="person">
      <p class="person-name">Dorian Vasko</p>
      <p class="person-title">Operations Manager</p>
    </div>
    <ul class="contact">
      <li>P.O. BOX 817 <span class="contact-dot"></span></li>
      <li>Glenn Dale, MD 20769 <span class="contact-dot"></span></li>
      <li>Office 301-555-0142 <span class="contact-dot"></span></li>
      <li>Cell 301-555-0187 <span class="contact-dot"></span></li>
      <li>Fax 301-555-0163 <span class="contact-dot"></span></li>
      <li>dorian@rktbuilders.example <span class="contact-dot"></span></li>
    </ul>
  </section>
</main>
</body>
</html>
```